Intelligent design image for our website

I would like an awesome image for our website that showcases the intelligent design of our app. We currently have a test web site here.
https://www.roadpliant.com.au/test-ewd/
I really do not like the graphic next to the "Intelligent design" and i want something much better than this.
Our app is used by Australian Truck Drivers. It would be nice to have a little bit of an Australian feel, but most importantly is should clearly showcase our app look a feel and the screens should be as legible (readable) as possible. These examples could be used for inspiration.
https://mockvendra.net/products/free-app-showcase-mockup-psd-5817402
https://www.plontrix.com/community/file/2294618830157362901/AppScreen-Intro-Page-Layout-for-Phone-Apps-Display

```html
<!DOCTYPE html>
<html lang="en">
<head>
<meta charset="utf-8">
<title>Roadpliant – Work Diary Screen</title>
<link rel="stylesheet" href="https://fonts.googleapis.com/css2?family=Lato:ital,wght@0,400;0,700;1,400;1,700&family=Tinos&display=swap">
<style>
  :root{
    --page:#f3f5f3;
    --screen:#ffffff;
    --ink:#111111;
    --muted:#6b6b6b;
    --accent:#2aa6e0;
    --line:#1f1fe0;
    --grid:#bdbdbd;
    --shade-dark:#d6d6d6;
    --shade-light:#ececec;
    --location:#dcdcdc;
  }
  *{box-sizing:border-box;margin:0;padding:0}
  html,body{width:1200px;height:1016px;overflow:hidden;background:var(--page)}
  body{font-family:"Lato",sans-serif;color:var(--ink);position:relative}
  .app-screen{position:absolute;left:0;top:210px;width:1200px;height:596px;background:var(--screen);border-radius:28px;box-shadow:0 10px 40px rgba(0,0,0,.08)}
  .toolbar{position:absolute;left:60px;top:30px;display:flex;gap:24px;align-items:center}
  .diary-date{position:absolute;right:120px;top:34px;font-size:20px;font-weight:700;font-style:italic}
  .driver-info{position:absolute;left:70px;top:92px;font-style:italic}
  .info-item{position:absolute;white-space:nowrap}
  .info-item .label{display:block;font-size:13px}
  .info-item .value{display:block;font-size:16px}
  .chart{position:absolute;left:0;top:0}
  .side-nav{position:absolute;right:40px;top:24px;width:40px;display:flex;flex-direction:column;align-items:center;gap:26px}
  .totals{position:absolute;top:518px;font-weight:700;font-style:italic;font-size:19px}
  .totals.work{left:66px}
  .totals.rest{left:470px}
  .device-note{position:absolute;left:66px;top:548px;font-size:12px;font-style:italic;color:var(--muted)}
  .udi{position:absolute;right:120px;top:540px;font-size:20px;color:var(--muted)}
  .home-bar{position:absolute;left:440px;top:572px;width:300px;height:6px;border-radius:3px;background:var(--ink)}
</style>
</head>
<body>
<main class="app-screen">
  <nav class="toolbar">
    <svg width="26" height="26" viewBox="0 0 26 26" aria-label="Back"><path d="M22 13H4M12 5l-8 8 8 8" fill="none" stroke="#111" stroke-width="2.2"/></svg>
    <svg width="30" height="32" viewBox="0 0 30 32" aria-label="Unlocked"><path d="M5 13V9a7 7 0 0 1 14 0" fill="none" stroke="var(--accent)" stroke-width="2"/><rect x="8" y="14" width="18" height="15" rx="2" fill="none" stroke="var(--accent)" stroke-width="2"/><rect x="15.5" y="19" width="3" height="5" fill="var(--accent)"/></svg>
    <svg width="34" height="28" viewBox="0 0 34 28" aria-label="Filters"><g fill="none" stroke="var(--accent)" stroke-width="2"><path d="M1 5h32M1 14h32M1 23h32"/><circle cx="12" cy="5" r="3" fill="#fff"/><circle cx="24" cy="14" r="3" fill="#fff"/><circle cx="9" cy="23" r="3" fill="#fff"/></g></svg>
  </nav>
  <div class="diary-date">Date: 28 Feb 2023</div>

  <section class="driver-info">
    <div class="info-item" style="left:0"><span class="label">Driver Name:</span><span class="value">Jack Turner</span></div>
    <div class="info-item" style="left:180px"><span class="label">Licence:</span><span class="value">1234567890</span></div>
    <div class="info-item" style="left:360px"><span class="label">Registration:</span><span class="value">III888</span></div>
    <div class="info-item" style="left:560px"><span class="label">Work Option:</span><span class="value">Standard Solo</span></div>
    <div class="info-item" style="left:770px"><span class="label">Timezone:</span><span class="value">NSW</span></div>
  </section>

  <svg class="chart" width="1200" height="520" viewBox="0 0 1200 520">
    <defs>
      <pattern id="quarter-ticks" width="9.6875" height="15" patternUnits="userSpaceOnUse" x="150" y="400">
        <path d="M9.2 2v11" stroke="#fff" stroke-width="1.4"/>
      </pattern>
    </defs>
    <g font-family="Lato, sans-serif" font-style="italic" font-size="15" fill="#111">
      <text x="140" y="173" text-anchor="end">Annotations</text>
      <text x="140" y="192" text-anchor="end">Comments</text>
      <text x="140" y="295" text-anchor="end">Location</text>
      <text x="110" y="420" text-anchor="end" font-size="14">2-up</text>
      <text x="110" y="450" text-anchor="end" font-size="14">Work</text>
      <text x="110" y="480" text-anchor="end" font-size="14">Rest</text>
    </g>
    <!-- annotation grid -->
    <g fill="none" stroke="#222" stroke-width="1">
      <rect x="150" y="152" width="930" height="50"/>
      <path d="M150 177H1080"/>
      <path d="M188.75 152v50M227.5 152v50M266.25 152v50M305 152v50M343.75 152v50M382.5 152v50M421.25 152v50M460 152v50M498.75 152v50M537.5 152v50M576.25 152v50M615 152v50M653.75 152v50M692.5 152v50M731.25 152v50M770 152v50M808.75 152v50M847.5 152v50M886.25 152v50M925 152v50M963.75 152v50M1002.5 152v50M1041.25 152v50"/>
    </g>
    <g font-size="18" text-anchor="middle" fill="#111">
      <text x="316.6" y="197">★</text><text x="448.4" y="197">★</text><text x="498.8" y="197">★</text>
      <text x="684.8" y="197">★</text><text x="735.1" y="197">★</text><text x="863" y="197">★</text>
    </g>
    <!-- location band -->
    <rect x="150" y="212" width="930" height="160" fill="var(--location)" stroke="#444"/>
    <g font-family="Tinos, serif" font-size="15" fill="#111">
      <text transform="translate(311,258) rotate(90)">Beresfield</text>
      <text transform="translate(443,258) rotate(90)">Goulburn</text>
      <text transform="translate(493,258) rotate(90)">Goulburn</text>
      <text transform="translate(679,248) rotate(90)">Wagga Wagga</text>
      <text transform="translate(729,248) rotate(90)">Wagga Wagga</text>
      <text transform="translate(857,255) rotate(90)">Shepparton</text>
    </g>
    <!-- hour labels -->
    <g font-family="Lato, sans-serif" font-size="14" text-anchor="middle" fill="#111">
      <text x="188.75" y="393">1</text><text x="227.5" y="393">2</text><text x="266.25" y="393">3</text><text x="305" y="393">4</text><text x="343.75" y="393">5</text><text x="382.5" y="393">6</text><text x="421.25" y="393">7</text><text x="460" y="393">8</text><text x="498.75" y="393">9</text><text x="537.5" y="393">10</text><text x="576.25" y="393">11</text><text x="615" y="393">12</text><text x="653.75" y="393">13</text><text x="692.5" y="393">14</text><text x="731.25" y="393">15</text><text x="770" y="393">16</text><text x="808.75" y="393">17</text><text x="847.5" y="393">18</text><text x="886.25" y="393">19</text><text x="925" y="393">20</text><text x="963.75" y="393">21</text><text x="1002.5" y="393">22</text><text x="1041.25" y="393">23</text><text x="1080" y="393">24</text>
    </g>
    <!-- activity grid -->
    <rect x="150" y="400" width="310" height="90" fill="var(--shade-dark)"/>
    <rect x="460" y="400" width="542.5" height="90" fill="var(--shade-light)"/>
    <rect x="1002.5" y="400" width="77.5" height="90" fill="var(--shade-dark)"/>
    <rect x="150" y="400" width="930" height="90" fill="url(#quarter-ticks)"/>
    <g stroke="var(--grid)" stroke-width="1" fill="none">
      <rect x="150" y="400" width="930" height="90"/>
      <path d="M150 430H1080M150 460H1080"/>
    </g>
    <path d="M150 478H295.3V445H430.9V478H469.7V445H644.1V478H692.5V445H799.1V478H1080" fill="none" stroke="var(--line)" stroke-width="3.5"/>
  </svg>

  <aside class="side-nav">
    <svg width="26" height="14" viewBox="0 0 26 14" aria-label="Scroll up"><path d="M2 12l11-10 11 10" fill="none" stroke="#ccc" stroke-width="1.5"/></svg>
    <svg width="38" height="26" viewBox="0 0 38 26" aria-label="Message"><g fill="none" stroke="var(--accent)" stroke-width="2"><rect x="1" y="1" width="36" height="24"/><path d="M1 1l18 14L37 1M1 25l13-12M37 25L24 13"/></g></svg>
    <svg width="36" height="36" viewBox="0 0 36 36" aria-label="Help"><circle cx="18" cy="18" r="16" fill="none" stroke="var(--accent)" stroke-width="2"/><text x="18" y="25" font-family="Lato, sans-serif" font-size="20" text-anchor="middle" fill="var(--accent)">?</text></svg>
    <svg width="38" height="38" viewBox="0 0 38 38" aria-label="Search"><g fill="none" stroke="var(--accent)" stroke-width="2.4"><circle cx="16" cy="16" r="13"/><path d="M25.5 25.5L36 36"/></g></svg>
    <svg width="38" height="38" viewBox="0 0 38 38" aria-label="Edit"><g fill="none" stroke="var(--accent)" stroke-width="2"><path d="M8 30L31 7l4 4-23 23-6 1z"/><path d="M2 37h34"/></g></svg>
    <svg width="40" height="36" viewBox="0 0 40 36" aria-label="Team"><g fill="none" stroke="var(--accent)" stroke-width="2"><circle cx="13" cy="10" r="7"/><circle cx="27" cy="10" r="7"/><path d="M2 35v-6a9 9 0 0 1 18 0v6zM20 35v-6a9 9 0 0 1 18 0v6z"/></g></svg>
    <svg width="30" height="40" viewBox="0 0 30 40" aria-label="Home location"><g fill="none" stroke="var(--accent)" stroke-width="2"><path d="M15 38C5 26 2 20 2 15a13 13 0 0 1 26 0c0 5-3 11-13 23z"/><path d="M9 15l6-5 6 5v6H9z"/></g></svg>
    <svg width="26" height="14" viewBox="0 0 26 14" aria-label="Scroll down"><path d="M2 2l11 10L24 2" fill="none" stroke="#ccc" stroke-width="1.5"/></svg>
  </aside>

  <div class="totals work">Work: 10hr, 45min</div>
  <div class="totals rest">Rest: 13hr, 15min</div>
  <div class="device-note">Device: &nbsp;Orchard, Pomephone XR, PomOS, 15.5.0</div>
  <div class="udi">UDI: NSW-67890-20010813</div>
  <div class="home-bar"></div>
</main>
</body>
</html>
```